A postcard needed for a kids gym

We are a kids gym opening soon. We are called Bouncewell Kids Gym. Here is the website so that you can get more details on what it is we will be doing. www.Bouncewellkidsgym.example I am including a screen shot of wallpaper we are using on two walls that will be prominently displayed in our building. I was wondering if the wall paper can somehow be included in the postcard as a soft background or something?no postage or mail info needed as this will be passed out by hand. I am also sending our logo and colors. Thank you for your help, and we look forward to hearing and seeing what you have to present. Sincerely,Lorraine

Target Market(s)

Parents

Industry/Entity Type

Childcare

Requirements
Must have
• "Opening soon"

```html
<!DOCTYPE html>
<html lang="en">
<head>
<meta charset="utf-8">
<title>Bouncewell Kids Gym – Opening Soon Postcard</title>
<link rel="stylesheet" href="https://fonts.googleapis.com/css2?family=Fredoka:wght@500;600&display=swap">
<style>
  :root {
    --sky-blue: #23a8e0;
    --ribbon-blue: #1f72bd;
    --ribbon-blue-light: #3d9ad8;
    --sunny-orange: #f9ad45;
    --paper-white: #ffffff;
    --tone-red: #d9283a;
    --tone-orange: #ee4a22;
    --tone-green: #25a24c;
    --tone-blue: #2f6fc8;
    --tone-purple: #7a2aa0;
  }
  * { margin: 0; padding: 0; box-sizing: border-box; }
  html, body {
    width: 1200px;
    height: 925px;
    overflow: hidden;
    background: var(--paper-white);
  }
  .postcard {
    position: relative;
    width: 1200px;
    height: 925px;
    overflow: hidden;
    font-family: "Fredoka", "Arial Rounded MT Bold", sans-serif;
  }
  .ball-pit-photo {
    position: absolute;
    inset: 0 0 auto 0;
    height: 700px;
    background: linear-gradient(120deg,
      var(--tone-orange) 0%,
      var(--tone-purple) 25%,
      var(--tone-red) 45%,
      var(--tone-green) 65%,
      var(--tone-blue) 85%,
      var(--tone-orange) 100%);
  }
  .wave-bands {
    position: absolute;
    inset: 0;
    width: 1200px;
    height: 925px;
  }
  .masking-tape {
    position: absolute;
    left: 32px;
    top: 472px;
    width: 136px;
    height: 296px;
    background: rgba(255, 255, 255, 0.85);
    transform: rotate(-1.5deg);
    box-shadow: 0 2px 6px rgba(0, 0, 0, 0.08);
  }
  .opening-ribbon {
    position: absolute;
    left: 150px;
    top: 560px;
    width: 515px;
    height: 102px;
    border-radius: 10px;
    background: linear-gradient(90deg, var(--ribbon-blue-light), var(--ribbon-blue));
    transform: rotate(-11.5deg);
    transform-origin: left top;
    box-shadow: 0 10px 16px rgba(0, 0, 0, 0.2);
    display: flex;
    align-items: center;
    padding-left: 58px;
  }
  .opening-ribbon__text {
    color: var(--paper-white);
    font-size: 58px;
    font-weight: 500;
    letter-spacing: 1px;
    line-height: 1;
  }
  .brand-name {
    position: absolute;
    left: 0;
    right: 0;
    top: 668px;
    text-align: center;
    color: var(--sky-blue);
    font-weight: 600;
    line-height: 1;
  }
  .brand-name__main {
    display: block;
    font-size: 132px;
    letter-spacing: -1px;
    padding-left: 10px;
  }
  .brand-name__sub {
    display: block;
    margin-top: 14px;
    font-size: 48px;
    letter-spacing: 4px;
    text-transform: uppercase;
  }
</style>
</head>
<body>
  <main class="postcard">
    <div class="ball-pit-photo" role="img" aria-label="Photograph of colourful ball-pit balls in red, orange, green, blue and purple"></div>

    <svg class="wave-bands" viewBox="0 0 1486 1123" preserveAspectRatio="none" aria-hidden="true">
      <path d="M0 745 Q 800 590 1486 745 L1486 1123 L0 1123 Z" fill="var(--sky-blue)"/>
      <path d="M0 782 Q 800 640 1486 790 L1486 1123 L0 1123 Z" fill="var(--sunny-orange)"/>
      <path d="M0 840 Q 800 680 1486 838 L1486 1123 L0 1123 Z" fill="var(--paper-white)"/>
    </svg>

    <div class="masking-tape" aria-hidden="true"></div>

    <div class="opening-ribbon">
      <span class="opening-ribbon__text">opening soon</span>
    </div>

    <h1 class="brand-name">
      <span class="brand-name__main">Bouncewell</span>
      <span class="brand-name__sub">Kids Gym</span>
    </h1>
  </main>
</body>
</html>
```